Property Maintenance business card design

I need a business card design for my business in Adelaide , South Australia called "Coastline Home Upkeep and Works".
I do All kinds of property maintenance. ie
Maintenance
Repairs
Handyman services
Gardening & Landscaping
Fencing
Renovations
Cleaning & Removals
Painting
Walls & Plastering
Doors & Windows

The colours I would like are : Black and gold

I would like my business card to look as professional as possible.

If theres any more information that you may need please let me know.

Im not sure weather this image i downloaded is any good but i like the house but also the three guys, more the house i think :)

Thanks.

Target Market(s)

real estate agents and the general public looking for handy work

Industry/Entity Type

House

Contact Information for Business Card

Gordon Falvey
Mobile: 0407352614
email: coastlinehu@examplemail.com

Requirements
Nice to have
• i would like the dot points of what i do to be on the back of the card if possible, or different designs of it on the back and it not on the back.

```html
<!DOCTYPE html>
<html lang="en">
<head>
<meta charset="utf-8">
<title>Coastline Home Upkeep and Works – Business Card</title>
<link rel="stylesheet" href="https://fonts.googleapis.com/css2?family=Arimo:wght@400;700&display=swap">
<style>
  :root {
    --backdrop: #8a8a8a;
    --card: #ffffff;
    --gold: #f2d024;
    --ink: #4a4a4a;
    --soft-ink: #7a7a7a;
    --photo-light: #f6f5f1;
    --photo-warm: #f1ebd6;
  }
  * { margin: 0; padding: 0; box-sizing: border-box; }
  html, body {
    width: 1200px;
    height: 901px;
    overflow: hidden;
    background: var(--backdrop);
    font-family: "Arimo", Arial, sans-serif;
  }
  .card {
    position: absolute;
    left: 75px;
    top: 150px;
    width: 1050px;
    height: 600px;
    background: var(--card);
    overflow: hidden;
    box-shadow: 0 6px 18px rgba(0,0,0,0.25);
  }
  .card__photo {
    position: absolute;
    left: 420px;
    top: 0;
    width: 630px;
    height: 600px;
    background:
      radial-gradient(ellipse at 40% 25%, var(--photo-warm) 0%, transparent 45%),
      radial-gradient(ellipse at 70% 60%, var(--photo-light) 0%, transparent 60%),
      linear-gradient(90deg, var(--card) 0%, var(--photo-light) 30%, var(--photo-light) 100%);
  }
  .brand {
    position: absolute;
    left: 40px;
    top: 110px;
    display: flex;
    align-items: center;
    gap: 22px;
  }
  .brand__mark {
    width: 90px;
    height: 90px;
    background: var(--gold);
  }
  .brand__name {
    color: var(--ink);
    font-size: 46px;
    font-weight: 400;
    line-height: 0.98;
    letter-spacing: 0.5px;
  }
  .holder {
    position: absolute;
    left: 40px;
    top: 395px;
    font-size: 58px;
    font-weight: 400;
    letter-spacing: -0.5px;
  }
  .holder__first { color: var(--gold); }
  .holder__last { color: var(--ink); }
  .rule {
    position: absolute;
    left: 40px;
    right: 0;
    top: 472px;
    height: 2px;
    background: var(--gold);
  }
  .contact {
    position: absolute;
    right: 40px;
    top: 395px;
    text-align: right;
    font-size: 22px;
    line-height: 1.35;
    color: var(--soft-ink);
  }
  .contact__label {
    color: var(--gold);
    font-weight: 700;
    margin-right: 6px;
  }
</style>
</head>
<body>
  <main class="card">
    <div class="card__photo" role="img" aria-label="Faded photo of tradespeople in hard hats holding tools"></div>

    <div class="brand">
      <div class="brand__mark"></div>
      <div class="brand__name">Coastline<br>Home<br>Upkeep<br>and Works</div>
    </div>

    <div class="holder"><span class="holder__first">Gordon</span><span class="holder__last">Falvey</span></div>

    <div class="contact">
      <div><span class="contact__label">Phone</span>0407352614</div>
      <div><span class="contact__label">Email</span>coastlinehu@examplemail.com</div>
    </div>

    <div class="rule"></div>
  </main>
</body>
</html>
```